Varnell Contracting In need of monthly newsletter

We need a monthly newsletter to promote our monthly special of Mulch Installation.

Please change wording to fit what you feel is professional and effective.

Our regular price to install Mulch is $169/Yard installed/Delivered

We would like to run a promotion of $125/Yard Installed & Delivered

Compare us to others $135/Yard Delivered only from some other suppliers

Also list somewhere on the newsletter :
- Delivery of soils, stone, wood also available
- Check out our website
- an emphasis on quality

The Fine Print
* Some Conditions apply
Mulches included in sale Onyx Velvet, Chocolate Brown, Auburn Red, Natural, Hemlock, Gold, Shredded Pine. Some site conditions may incur extra cost. minimum 3 Yards for sale price to be in effect, HST extra on all prices listed,

CHECK OUR WEBSITE FOR SOME IMAGES AND MORE INFORMATION....

ASK ANYTHING YOU WANT VIA Draft Plaza
Updates

Types of Mulch have changed Slightly in the "Fine Print"

Classic Cedar, Black Cedar, Red Cedar, Chocolate brown, Pine Bark, Natural Shredded Pine, Hemlock, Utility Style.

We will also be submitting pictures of the mulch HOWEVER you might need to crop or alter these images to make them work for our newsletter.

Project Deadline Extended
Reason: We have not yet found a design we think is Straight to the point. Simple and with our theme.

```html
<!DOCTYPE html>
<html lang="en">
<head>
<meta charset="utf-8">
<title>Varnell Contracting – Mulch Installation Special Month</title>
<link href="https://fonts.googleapis.com/css2?family=Ubuntu:ital,wght@0,300;0,400;0,500;0,700;1,400&family=Open+Sans:wght@400;600;700&display=swap" rel="stylesheet">
<style>
  :root {
    --backdrop: #8d8d8d;
    --cream: #e6dfcf;
    --orange: #e0783a;
    --orange-light: #f3a45c;
    --orange-deep: #c9531f;
    --band: #d5581f;
    --red-pill: #c8401f;
    --brown: #8a6538;
    --brown-dark: #5e4124;
    --ink: #3a2414;
    --white: #fff8ee;
    --garden-dark: #2e2a1c;
    --garden-green: #4f7a2e;
    --mulch: #4a2f1c;
  }
  * { box-sizing: border-box; margin: 0; padding: 0; }
  html, body { width: 1200px; height: 1000px; overflow: hidden; }
  body {
    background: var(--backdrop);
    font-family: "Open Sans", Arial, sans-serif;
    position: relative;
  }
  .flyer {
    position: absolute; left: 270px; top: 30px;
    width: 660px; height: 940px;
    background: var(--cream);
    padding: 14px;
    box-shadow: 0 10px 30px rgba(0,0,0,.35);
  }
  .flyer__inner {
    position: relative; width: 100%; height: 100%; overflow: hidden;
    background: radial-gradient(ellipse at 30% 45%, var(--orange-light) 0%, var(--orange) 45%, var(--orange-deep) 100%);
  }
  .brand {
    position: absolute; left: 24px; top: 26px;
    display: flex; align-items: center; gap: 12px;
  }
  .brand__dot {
    width: 62px; height: 62px; border-radius: 50%;
    background: var(--orange-deep);
  }
  .brand__name {
    font-family: "Ubuntu", Arial, sans-serif; font-weight: 500;
    color: var(--ink); font-size: 22px; line-height: 1.05; letter-spacing: 1px;
    text-transform: uppercase;
  }
  .header-rule {
    position: absolute; left: 250px; right: 60px; top: 92px;
    height: 2px; background: var(--orange-deep);
  }
  .header-band {
    position: absolute; left: 0; right: 0; top: 116px; height: 34px;
    background: var(--band);
  }
  .photo {
    position: absolute;
    background: linear-gradient(160deg, var(--garden-green), var(--garden-dark));
  }
  .photo--hero { left: 150px; right: 0; top: 150px; height: 300px;
    background: linear-gradient(120deg, #d9d4c8 0%, #6f8f3c 35%, var(--garden-dark) 60%, #a04a32 85%, #d98fb8 100%); }
  .photo--mulch-hands { left: 420px; right: 0; top: 450px; height: 130px;
    background: linear-gradient(160deg, #6d8fb5, var(--mulch)); }
  .photo--garden-bed { left: 420px; right: 0; top: 612px; height: 100px;
    background: linear-gradient(160deg, #7ba33e, var(--mulch)); }
  .photo--tree-bed { left: 420px; right: 0; top: 744px; height: 168px;
    background: linear-gradient(160deg, #6b4a2f, #3a2618); }
  .caption {
    position: absolute; left: 420px; right: 0; height: 32px;
    background: var(--orange-deep);
    color: var(--white); font-size: 12px; font-weight: 600;
    padding: 8px 0 0 30px;
  }
  .caption--first { top: 580px; }
  .caption--second { top: 712px; }
  .caption--third { top: 880px; }
  .seal {
    position: absolute; right: 26px; top: 66px;
    width: 104px; height: 104px; border-radius: 50%;
    background: var(--orange); border: 5px solid var(--brown-dark);
    display: flex; flex-direction: column; align-items: center; justify-content: center;
    font-family: "Ubuntu", Arial, sans-serif; color: var(--ink); text-align: center;
  }
  .seal__stars { font-size: 9px; color: var(--white); letter-spacing: 2px; }
  .seal__title { font-weight: 700; font-size: 16px; line-height: 1; }
  .seal__pct { font-size: 11px; color: var(--white); margin-top: 3px; }
  .title-panel {
    position: absolute; left: 30px; top: 300px; width: 380px; height: 130px;
    background: rgba(214, 108, 50, .88);
    font-family: "Ubuntu", Arial, sans-serif; color: var(--white);
    text-align: center; padding-top: 24px;
  }
  .title-panel__line1 { font-size: 32px; font-weight: 500; letter-spacing: .5px; }
  .title-panel__line2 { font-size: 32px; font-weight: 700; }
  .price-ribbon { position: absolute; left: 14px; top: 432px; width: 440px; height: 96px; }
  .price-ribbon svg { position: absolute; inset: 0; }
  .price-ribbon__amount {
    position: absolute; left: 30px; top: 6px;
    font-family: "Ubuntu", Arial, sans-serif; font-weight: 300;
    font-size: 66px; color: var(--white);
  }
  .price-ribbon__note {
    position: absolute; left: 232px; top: 30px;
    font-family: "Ubuntu", Arial, sans-serif; font-size: 21px; line-height: 1.05; color: var(--white);
  }
  .offer { position: absolute; left: 14px; width: 412px; text-align: center; color: var(--white); white-space: nowrap; }
  .offer--regular { top: 540px; font-family: "Ubuntu", Arial, sans-serif; font-style: italic; font-size: 14.5px; line-height: 20px; }
  .offer--compare { top: 568px; font-size: 11px; font-weight: 600; line-height: 1.4; }
  .delivery-pill {
    position: absolute; left: 34px; top: 612px; width: 372px; height: 46px;
    background: var(--red-pill); border-radius: 23px;
    color: var(--white); font-weight: 700; font-size: 16px;
    display: flex; align-items: center; justify-content: center;
    box-shadow: 0 3px 6px rgba(0,0,0,.3);
  }
  .phone {
    position: absolute; left: 30px; width: 380px; top: 676px; text-align: center;
    font-family: "Ubuntu", Arial, sans-serif; font-weight: 700; font-size: 30px; color: var(--ink);
  }
  .trust { position: absolute; left: 40px; top: 730px; display: flex; gap: 8px; align-items: center; }
  .trust__badge { width: 46px; height: 30px; background: #3b5b8c; border-radius: 3px; }
  .trust__card { width: 40px; height: 28px; background: var(--white); border-radius: 3px; }
  .contact {
    position: absolute; left: 200px; top: 728px; font-size: 12px; line-height: 1.45; color: var(--brown-dark);
  }
  .fine-print {
    position: absolute; left: 30px; top: 782px; width: 380px;
    font-size: 11px; line-height: 1.45; color: var(--white);
  }
</style>
</head>
<body>
  <article class="flyer">
    <div class="flyer__inner">
      <div class="brand">
        <span class="brand__dot"></span>
        <span class="brand__name">Varnell<br>Contracting<br>Group</span>
      </div>
      <div class="header-rule"></div>
      <div class="header-band"></div>

      <div class="photo photo--hero" role="img" aria-label="Landscaped garden with curved stone path, dark mulch beds, shrubs and pink flowers by a brick house"></div>

      <div class="seal">
        <span class="seal__stars">★★★★★</span>
        <span class="seal__title">Premium<br>Quality</span>
        <span class="seal__pct">100%</span>
      </div>

      <div class="title-panel">
        <div class="title-panel__line1">MULCH INSTALLATION</div>
        <div class="title-panel__line2">Special Month</div>
      </div>

      <div class="price-ribbon">
        <svg viewBox="0 0 440 96" width="440" height="96" aria-hidden="true">
          <polygon points="0,10 440,0 410,48 440,96 0,86" fill="var(--brown)"/>
          <polygon points="0,86 16,86 16,96" fill="var(--brown-dark)"/>
        </svg>
        <span class="price-ribbon__amount">$125</span>
        <span class="price-ribbon__note">Yard Installed<br>&amp; Delivered</span>
      </div>

      <p class="offer offer--regular">Our regular price is $169, Yard Installed &amp; Delivered</p>
      <p class="offer offer--compare">Compare us to others<br>$135 Yard Delivered only from some other suppliers</p>

      <div class="delivery-pill">Delivery of soils, stone, wood also available!</div>

      <div class="phone">555.014.2290</div>

      <div class="trust">
        <span class="trust__badge"></span>
        <span class="trust__card"></span>
        <span class="trust__card"></span>
      </div>
      <div class="contact">info@varnellcontracting.com<br>www.varnellcontracting.com</div>

      <p class="fine-print">Mulches included in sale Onyx Velvet, Chocolate Brown, Auburn Red, Natural, Hemlock, Gold, Shredded Pine. Some site conditions may incur extra cost, minimum 3 Yards for sale price to be in effect, HST extra on all prices listed.</p>

      <div class="photo photo--mulch-hands" role="img" aria-label="Two hands holding a pile of shredded brown mulch"></div>
      <div class="caption caption--first">(SOME TEXT HERE)</div>
      <div class="photo photo--garden-bed" role="img" aria-label="Freshly mulched garden bed with rows of small shrubs"></div>
      <div class="caption caption--second">(SOME TEXT HERE)</div>
      <div class="photo photo--tree-bed" role="img" aria-label="Hand spreading mulch around the base of a tree"></div>
      <div class="caption caption--third">(SOME TEXT HERE)</div>
    </div>
  </article>
</body>
</html>
```